Northway Living, mobile, wordpress website

Do you want to directly, and in a big way, create a simple, beautiful, new, innovative lifestyle sports social & mobile site that reflects while grows a emerging community, lifestyle and movement.
A community of not just like-minded individuals and groups, (not just referring to just sports fans, in fact, if you’re not a sports fan, not a big deal) but a community built around numerous shared cultural passions- on and offline.
A site built around not just the universal appeal of sports and celebrity, even celebrity sports fans, but with the potential to become a leader in the transformative movement that’s already begun to shape and drive society and the future. This product, it's informative nature, culture shaping and driving service and community will be as insightful and informative as it will be about entertainment. It will be known for producing and covering big, global events.
Think FUN, irreverent and smart. Think Brevin, Tam Velloza, and a little edgy, like Dirk Wenslow not being completely alienating and bombastic, all sharing funny stuff and thoughts.
Do you want to bring your fresh perspective, while gaining incredible experience, developing key skills, practical knowledge and know how? Bringing to the team your next-generation, Millennial knowledge about the latest mobile technology, and how to most effectively take advantage of this valuable expertise? We know you've got it, and would love what you come up with. Not flashy. Clean, simple background, tons of video displayed in creative, addicting ways. A layout design like http://www.flickcove.example/
The final design should express a site and community that immediately says it's like no other sports site that exists today, while at the same time demonstrating it's where the future of sports is heading.
Updates
Project Deadline Extended
Reason: Due to the Holiday Season, designers demonstrated it was not the best time of year for the contest. We want to give a chance for more designers to participate and designers we are interested in a chance to do modifications.
Target Market(s)
Male 18-34, urban, educated, with disposable income.
Industry/Entity Type
Community
Requirements
Must have
- mobile-optimizing.

```html
<!DOCTYPE html>
<html lang="en">
<head>
<meta charset="utf-8">
<title>Northway Living</title>
<link rel="stylesheet" href="https://fonts.googleapis.com/css2?family=Marcellus&family=Abel&family=Questrial&display=swap">
<style>
:root{
  --red:#cc1620;
  --blue:#1e98c6;
  --blue-line:#4fb2d8;
  --black:#050505;
  --white:#ffffff;
  --paper:#f4f4f4;
  --ink:#1b2733;
  --muted:#555;
  --serif:'Marcellus', serif;
  --sans:'Abel', sans-serif;
  --body:'Questrial', sans-serif;
}
*{margin:0;padding:0;box-sizing:border-box}
html,body{width:1200px;height:1125px;overflow:hidden}
body{position:relative;background:var(--paper);font-family:var(--body);color:var(--ink)}
.abs{position:absolute}

/* header */
.site-header{left:0;top:0;width:1200px;height:170px;background:linear-gradient(#fafafa,#f1f1f1)}
.brand-name{left:101px;top:56px;font-family:var(--serif);font-size:46px;line-height:56px;color:var(--ink);letter-spacing:.5px;white-space:nowrap}
.cart{left:909px;top:0;width:201px;height:66px;background:var(--black);color:var(--white);display:flex;align-items:center;justify-content:center;gap:14px;font-family:var(--sans);font-size:22px;letter-spacing:1px}
.cart b{font-weight:400;color:var(--blue)}
.sale{left:909px;top:66px;width:201px;height:67px;background:var(--blue);color:var(--white);display:flex;align-items:center;justify-content:center;gap:30px;font-family:var(--sans);font-size:20px;letter-spacing:2px;text-align:center;line-height:22px}

/* nav */
.main-nav{left:0;top:170px;width:1200px;height:55px;background:var(--black)}
.main-nav a{position:absolute;top:0;line-height:55px;transform:translateX(-50%);color:var(--white);text-decoration:none;font-family:var(--serif);font-size:23px;letter-spacing:.5px;white-space:nowrap}

/* top news */
.top-news{left:0;top:225px;width:1200px;height:466px;background:var(--red)}
.top-news h2{position:absolute;left:165px;top:46px;font-family:var(--serif);font-weight:400;font-size:38px;color:var(--white)}
.slide-media{left:164px;top:127px;width:466px;height:265px;background:linear-gradient(90deg,#d9d9d9 0%,#d2d2d2 55%,#6c6c6c 78%,#2a2a2a 100%)}
.slide-card{left:630px;top:128px;width:404px;height:264px;background:var(--white);border-top:10px solid var(--black);box-shadow:0 4px 10px rgba(0,0,0,.3);padding:14px 18px 0 20px}
.slide-card h3{font-family:var(--serif);font-weight:400;font-size:37px;line-height:40px;color:var(--black);white-space:nowrap}
.slide-card .tagline{font-family:var(--serif);font-size:14px;color:var(--muted);letter-spacing:.8px}
.slide-card p.excerpt{margin-top:20px;font-size:11.6px;line-height:17px;text-align:justify;color:#222;letter-spacing:0}
.read-more{display:block;margin-top:7px;font-family:var(--sans);font-size:15px;color:var(--blue);text-decoration:none}
.share{position:absolute;top:217px;height:21px;border-radius:4px;font-size:11px;color:var(--white);display:flex;align-items:center;padding-left:8px;font-family:var(--body);white-space:nowrap}
.share span{margin-left:auto;height:17px;margin-right:2px;background:var(--white);color:#333;border-radius:3px;padding:0 4px;line-height:17px;font-size:10.5px}
.share.chirp{left:20px;width:76px;background:linear-gradient(#8fd3f5,#3ba7e0)}
.share.link{left:154px;width:89px;background:linear-gradient(#6f95d6,#3b63b4)}
.share.beacon{left:300px;width:86px;background:linear-gradient(#f47b63,#d9351d)}
.arrow{width:38px;height:38px}

/* feed */
.feed{left:96px;top:691px;width:1014px;height:434px;background:var(--blue)}
.filters{position:absolute;left:84px;top:33px;width:840px;height:30px}
.filters a{position:absolute;top:0;line-height:30px;font-family:var(--sans);font-size:21px;color:var(--white);text-decoration:none;letter-spacing:1px;white-space:nowrap}
.filters a.active{background:var(--white);color:var(--black);padding:0 8px}
.rule{position:absolute;left:84px;top:85px;width:840px;height:1px;background:var(--blue-line)}
.post{position:absolute;top:129px;width:281px}
.post .thumb{width:281px;height:205px}
.post h4{margin-top:7px;font-family:var(--sans);font-weight:400;font-size:21px;color:var(--white);letter-spacing:.5px;white-space:nowrap}
.post .meta{display:flex;align-items:center;font-family:var(--sans);font-size:21px;letter-spacing:.5px}
.post .meta a{color:var(--ink);text-decoration:none}
.post .likes{margin-left:auto;display:flex;align-items:center;gap:6px;color:var(--white);font-size:18px}
</style>
</head>
<body>

<header class="site-header abs">
  <div class="brand-name abs">Northway Living</div>
  <a class="cart abs">
    <svg width="46" height="38" viewBox="0 0 46 38" aria-hidden="true"><path d="M2 4h7l6 20h22l5-14H12" fill="none" stroke="#fff" stroke-width="4" stroke-linejoin="round"/><path d="M17 15h22M19 20h17" stroke="#fff" stroke-width="3"/><circle cx="18" cy="32" r="3.5" fill="#fff"/><circle cx="34" cy="32" r="3.5" fill="#fff"/></svg>
    <span>0 <b>ITEMS</b></span>
  </a>
  <a class="sale abs">
    <svg width="40" height="46" viewBox="0 0 40 46" aria-hidden="true"><path d="M4 14h32l2 30H2z" fill="#fff"/><path d="M13 18v-8a7 7 0 0 1 14 0v8" fill="none" stroke="#1e98c6" stroke-width="3"/></svg>
    <span>30%<br>SALE</span>
  </a>
</header>

<nav class="main-nav abs">
  <a style="left:150px">HOME</a>
  <a style="left:318px">ARTICLES</a>
  <a style="left:504px">RESEARCH</a>
  <a style="left:684px">TEAM</a>
  <a style="left:852px">EVENTS</a>
  <a style="left:1029px">CONTACT</a>
</nav>

<section class="top-news abs">
  <h2>TOP NEWS</h2>
  <svg class="arrow abs" style="left:107px;top:237px" viewBox="0 0 38 38" aria-label="Previous"><circle cx="19" cy="19" r="19" fill="#fff"/><path d="M10 19l9-9v6h9v6h-9v6z" fill="#cc1620"/></svg>
  <div class="slide-media abs" role="img" aria-label="Featured story photo: fashion photography promo with black-and-white portrait"></div>
  <article class="slide-card abs">
    <h3>Browse Sections</h3>
    <div class="tagline">The best content is just a flip away</div>
    <p class="excerpt">Explore recommended reading in the Content Guide, including major publications.Explore recommended reading in the Content Guide, including major publications.Explore recommended reading in the Content Guide, including major publications.</p>
    <a class="read-more">&gt;&gt; READ MORE</a>
    <div class="share chirp">Chirpline<span>20</span></div>
    <div class="share link">Linkyard<span>40</span></div>
    <div class="share beacon">Beacon +<span>100</span></div>
  </article>
  <svg class="arrow abs" style="left:1057px;top:237px" viewBox="0 0 38 38" aria-label="Next"><circle cx="19" cy="19" r="19" fill="#fff"/><path d="M28 19l-9-9v6h-9v6h9v6z" fill="#cc1620"/></svg>
</section>

<section class="feed abs">
  <nav class="filters">
    <a class="active" style="left:0">ALL</a>
    <a style="left:71px">COMICS</a>
    <a style="left:174px">COSPLAY</a>
    <a style="left:297px">FILM</a>
    <a style="left:375px">GAMES</a>
    <a style="left:475px">MUSIC</a>
    <a style="left:567px">NEWS</a>
    <a style="left:657px">REVIEW</a>
    <a style="left:764px">SCIENCE</a>
  </nav>
  <div class="rule"></div>

  <article class="post" style="left:55px">
    <div class="thumb" role="img" aria-label="Photo of a lit theatre marquee on a city street at dusk" style="background:linear-gradient(160deg,#6f8fb0 0%,#8a5a3a 50%,#b23a1c 80%,#e0a04a 100%)"></div>
    <h4>GYROLINK IS A 3D MOUSE</h4>
    <div class="meta"><a>READ MORE</a><span class="likes"><svg width="18" height="16" viewBox="0 0 18 16" aria-hidden="true"><path d="M9 16L1.5 8.5A4.3 4.3 0 0 1 9 3a4.3 4.3 0 0 1 7.5 5.5z" fill="#9fd3ea"/></svg>50</span></div>
  </article>

  <article class="post" style="left:371px">
    <div class="thumb" role="img" aria-label="Flat cartoon illustration of a red character on a yellow background" style="background:linear-gradient(135deg,#f6d57c 0%,#f6d57c 35%,#d8442a 60%,#f6d57c 100%)"></div>
    <h4>GYROLINK IS A 3D MOUSE</h4>
    <div class="meta"><a>READ MORE</a><span class="likes"><svg width="18" height="16" viewBox="0 0 18 16" aria-hidden="true"><path d="M9 16L1.5 8.5A4.3 4.3 0 0 1 9 3a4.3 4.3 0 0 1 7.5 5.5z" fill="#9fd3ea"/></svg>50</span></div>
  </article>

  <article class="post" style="left:682px">
    <div class="thumb" role="img" aria-label="Photo of a small blue 3D-printed tower model on a table" style="background:linear-gradient(180deg,#3a3936 0%,#6b6660 45%,#a39e97 75%,#8b8580 100%)"></div>
    <h4>GYROLINK IS A 3D MOUSE</h4>
    <div class="meta"><a>READ MORE</a><span class="likes"><svg width="18" height="16" viewBox="0 0 18 16" aria-hidden="true"><path d="M9 16L1.5 8.5A4.3 4.3 0 0 1 9 3a4.3 4.3 0 0 1 7.5 5.5z" fill="#9fd3ea"/></svg>50</span></div>
  </article>
</section>

</body>
</html>
```